Velmaran Business Card

Business card for philanthropic organization

Industry/Entity Type

Business

Contact Information for Business Card

Need a very ELEGANT, sober, embossed, formal business card... it should transmit CREDIBILITY. Not looking for a "fun card". would like white, grays or black designs.

Font styles to use
Script

Requirements
Must have
• Embossed look

```html
<!DOCTYPE html>
<html lang="en">
<head>
<meta charset="utf-8">
<title>Velmaran Business Card</title>
<link href="https://fonts.googleapis.com/css2?family=Pinyon+Script&family=Roboto:wght@400;500;700&display=swap" rel="stylesheet">
<style>
  :root {
    --page-bg: #e9e9ea;
    --card-white: #fbfbfb;
    --band-top: #8d8d92;
    --band-bottom: #e2e2e4;
    --fold-grey: #c4c4c8;
    --fold-light: #ffffff;
    --name-ink: #141416;
    --ink: #1c1c1f;
    --mark-grey: #3c3c40;
    --emboss-light: rgba(255,255,255,0.75);
    --emboss-dark: rgba(0,0,0,0.35);
  }
  * { margin: 0; padding: 0; box-sizing: border-box; }
  html, body {
    width: 1200px; height: 1200px; overflow: hidden;
    background: var(--page-bg);
    font-family: "Roboto", Arial, sans-serif;
  }
  .card {
    position: absolute;
    left: 100px; top: 315px;
    width: 1000px; height: 570px;
    background: var(--card-white);
    box-shadow: 0 12px 30px rgba(0,0,0,0.18), inset 0 0 0 1px rgba(0,0,0,0.06);
    overflow: hidden;
  }
  .card-band { position: absolute; inset: 0; }
  .brand {
    position: absolute;
    left: 580px; top: 112px;
    transform: translateX(-50%);
    display: flex; align-items: center; gap: 12px;
    color: var(--mark-grey);
    font-weight: 500; font-size: 34px; letter-spacing: 2px;
  }
  .brand-dot {
    width: 20px; height: 20px; border-radius: 50%;
    background: var(--mark-grey);
  }
  .holder {
    position: absolute; left: 80px; top: 282px;
    color: var(--ink);
  }
  .holder-name {
    font-family: "Pinyon Script", cursive;
    font-weight: 400;
    color: var(--name-ink);
    font-size: 66px; line-height: 1.05;
    text-shadow: 0 1px 0 var(--emboss-light), 0 -1px 0 var(--emboss-dark);
  }
  .holder-role {
    font-size: 25px; line-height: 1.25; margin-left: 10px;
    text-shadow: 0 1px 0 var(--emboss-light);
  }
  .contact {
    position: absolute; left: 610px; top: 385px;
    list-style: none; color: var(--ink);
    font-size: 22px; font-weight: 500; line-height: 1.3;
    text-shadow: 0 1px 0 var(--emboss-light);
  }
  .contact li { display: flex; align-items: flex-start; gap: 10px; margin-bottom: 8px; }
  .contact svg { width: 22px; height: 22px; flex: none; margin-top: 2px; }
</style>
</head>
<body>
  <article class="card">
    <svg class="card-band" viewBox="0 0 1000 570" aria-hidden="true">
      <defs>
        <linearGradient id="greyBand" x1="0" y1="0" x2="0" y2="1">
          <stop offset="0" stop-color="var(--band-top)"/>
          <stop offset="1" stop-color="var(--band-bottom)"/>
        </linearGradient>
      </defs>
      <path d="M0,198 Q520,318 1000,236 L1000,570 L0,570Z" fill="var(--fold-grey)"/>
      <path d="M0,210 Q520,334 1000,254 L1000,570 L0,570Z" fill="var(--fold-light)" opacity="0.7"/>
      <path d="M0,214 Q520,338 1000,258 L1000,570 L0,570Z" fill="url(#greyBand)"/>
    </svg>

    <div class="brand"><span class="brand-dot"></span>Velmaran</div>

    <div class="holder">
      <h1 class="holder-name">Damián Quiroga</h1>
      <p class="holder-role">Almar Qadi Velmaran</p>
      <p class="holder-role">Potentate 2017</p>
    </div>

    <ul class="contact">
      <li>
        <svg viewBox="0 0 24 24"><path fill="currentColor" d="M6.6 10.8a15 15 0 0 0 6.6 6.6l2.2-2.2a1 1 0 0 1 1-.25 11 11 0 0 0 3.6.6 1 1 0 0 1 1 1V20a1 1 0 0 1-1 1A17 17 0 0 1 3 4a1 1 0 0 1 1-1h3.5a1 1 0 0 1 1 1 11 11 0 0 0 .6 3.6 1 1 0 0 1-.25 1z"/></svg>
        <span>+(507)-6000-0142</span>
      </li>
      <li>
        <svg viewBox="0 0 24 24"><text x="12" y="19" font-size="22" font-weight="700" text-anchor="middle" fill="currentColor" font-family="Roboto, sans-serif">@</text></svg>
        <span>dquiroga@velmaran.org</span>
      </li>
      <li>
        <svg viewBox="0 0 24 24"><path fill="currentColor" d="M12 2a7 7 0 0 0-7 7c0 5.2 7 13 7 13s7-7.8 7-13a7 7 0 0 0-7-7zm0 9.5A2.5 2.5 0 1 1 12 6.5a2.5 2.5 0 0 1 0 5z"/></svg>
        <span>P.O. Box 0000-01234<br>Panama, Republic of Panama</span>
      </li>
    </ul>
  </article>
</body>
</html>
```